Web Developer Needs a Business Card Design

I need a personal business card design that represents me as a web developer for potential employers. I would like the background to be a dark color on the front for contrast with my logo and name. The back will have all my information along with a smaller version of the logo. I want something with a modern look and feel, not too conservative. This will be used for potential employers and freelance work.

Industry/Entity Type

Business

Contact Information for Business Card

Front should have my logo and name. The back should have all my personal information which would include: name: Tom Brevardi, phone: 570-614-9083, email: tombrevardi@mailwisp.com, website url: www.tombrevardi.com, logo, web developer.

Font styles to use
Sans Serif

Requirements
Must have
• Must include my logo. The color palette base color will be the logo color.

```html
<!DOCTYPE html>
<html lang="en">
<head>
<meta charset="utf-8">
<title>Tom Brevardi — Business Card</title>
<link href="https://fonts.googleapis.com/css2?family=Raleway:wght@400;500;600&display=swap" rel="stylesheet">
<style>
  :root {
    --stage: #0d0d0d;
    --teal: #67c5b2;
    --teal-light: #4fb4a6;
    --teal-deep: #2a6b63;
    --paper: #ffffff;
    --accent-yellow: #dfe06e;
    --card-w: 1000px;
    --card-h: 572px;
  }
  * { margin: 0; padding: 0; box-sizing: border-box; }
  html, body {
    width: 1200px;
    height: 3600px;
    overflow: hidden;
    background: var(--stage);
    font-family: "Raleway", sans-serif;
  }
  .sheet {
    width: 1200px;
    height: 3600px;
    display: flex;
    flex-direction: column;
    align-items: center;
    justify-content: center;
    gap: 300px;
  }
  .card {
    width: var(--card-w);
    height: var(--card-h);
    position: relative;
    overflow: hidden;
  }
  .card svg { display: block; width: 100%; height: 100%; }
  .card-front {
    background: radial-gradient(ellipse at 50% 38%, var(--teal-light) 0%, #3a8d83 40%, var(--teal-deep) 100%);
  }
  .card-back { background: var(--paper); }
  .brand-name { font-family: "Raleway", sans-serif; font-weight: 500; }
  .info-name { font-family: "Raleway", sans-serif; font-weight: 500; }
  .info-role { font-family: "Raleway", sans-serif; font-weight: 400; }
  .info-line { font-family: "Raleway", sans-serif; font-weight: 400; }
  .icon-letter { font-family: "Raleway", sans-serif; font-weight: 600; }
</style>
</head>
<body>
<main class="sheet">

  <section class="card card-front" aria-label="Card front">
    <svg viewBox="0 0 1000 572" xmlns="http://www.w3.org/2000/svg">
      <circle class="brand-mark" cx="500" cy="230" r="72" fill="none" stroke="var(--paper)" stroke-width="12"/>
      <text class="brand-name" x="500" y="372" text-anchor="middle" font-size="40" fill="var(--paper)">Tom Brevardi</text>
    </svg>
  </section>

  <section class="card card-back" aria-label="Card back">
    <svg viewBox="0 0 1000 572" xmlns="http://www.w3.org/2000/svg">
      <path class="panel-curve-line" d="M 398 0 Q 300 286 452 572" fill="none" stroke="var(--teal)" stroke-width="6"/>
      <path class="info-panel" d="M 428 0 Q 330 286 482 572 L 1000 572 L 1000 0 Z" fill="var(--teal)"/>

      <circle class="brand-mark" cx="190" cy="235" r="82" fill="none" stroke="var(--teal)" stroke-width="14"/>
      <text class="brand-name" x="190" y="375" text-anchor="middle" font-size="30" fill="var(--teal)">Tom Brevardi</text>

      <text class="info-name" x="560" y="160" font-size="50" fill="var(--paper)">Tom Brevardi</text>
      <text class="info-role" x="562" y="196" font-size="26" fill="var(--accent-yellow)">web developer</text>

      <g class="contact-row" transform="translate(578 275)">
        <circle r="19" fill="none" stroke="var(--paper)" stroke-width="3"/>
        <text class="icon-letter" y="8" text-anchor="middle" font-size="22" fill="var(--paper)">p</text>
        <text class="info-line" x="36" y="8" font-size="23" fill="var(--paper)">570-614-9083</text>
      </g>
      <g class="contact-row" transform="translate(578 340)">
        <circle r="19" fill="none" stroke="var(--paper)" stroke-width="3"/>
        <text class="icon-letter" y="7" text-anchor="middle" font-size="22" fill="var(--paper)">e</text>
        <text class="info-line" x="36" y="8" font-size="23" fill="var(--paper)">tombrevardi@mailwisp.com</text>
      </g>
      <g class="contact-row" transform="translate(578 405)">
        <circle r="19" fill="none" stroke="var(--paper)" stroke-width="3"/>
        <text class="icon-letter" y="7" text-anchor="middle" font-size="20" fill="var(--paper)">w</text>
        <text class="info-line" x="36" y="8" font-size="23" fill="var(--paper)">www.tombrevardi.com</text>
      </g>
    </svg>
  </section>

</main>
</body>
</html>
```